Legal Stationary

A full set of stationery is required
The image and logo, along with colour, are set and attached.
The style should be modern, clean, and corporate. Not just a basic template off the web.
In addition to the address/website/email/phone fields for DX and KWT number, with the text “the firm is authorised and regulated by the KWT”
All files in all formats will be needed to allow editing after. Initial setup of templates will be required, and details for 4 business cards will be supplied.
Target Market(s)
Consumers of legal services
Industry/Entity Type
Legal

```html
<!DOCTYPE html>
<html lang="en">
<head>
<meta charset="utf-8">
<title>Halden Law – Business Card</title>
<link href="https://fonts.googleapis.com/css2?family=Montserrat:wght@400;500;700&display=swap" rel="stylesheet">
<style>
  :root {
    --brand-blue: #253b96;
    --brand-blue-soft: #5a6cc0;
    --ink: #1d1d1f;
    --paper: #ffffff;
    --backdrop: #e6e7ea;
  }
  * { box-sizing: border-box; margin: 0; padding: 0; }
  html, body { width: 1200px; height: 874px; overflow: hidden; }
  body {
    background: var(--backdrop);
    font-family: "Montserrat", sans-serif;
    display: flex;
    align-items: center;
    justify-content: center;
    gap: 40px;
  }
  .card {
    width: 540px;
    height: 310px;
    border-radius: 22px;
    position: relative;
    box-shadow: 0 6px 18px rgba(0,0,0,0.12);
  }
  /* Front face */
  .card-front { background: var(--brand-blue); color: var(--paper); }
  .front-logo {
    position: absolute;
    top: 96px; left: 0; right: 0;
    display: flex; align-items: center; justify-content: center; gap: 16px;
    color: var(--brand-blue-soft);
    font-weight: 700; font-size: 64px; letter-spacing: 1px;
  }
  .front-logo .mark { width: 30px; height: 30px; background: var(--brand-blue-soft); }
  .regulation-note {
    position: absolute; bottom: 34px; left: 0; right: 0;
    text-align: center; font-size: 14px; font-weight: 400; letter-spacing: 0.3px;
  }
  /* Back face */
  .card-back { background: var(--paper); color: var(--ink); }
  .back-logo {
    position: absolute; left: 36px; top: 128px;
    display: flex; align-items: center; gap: 10px;
    color: var(--brand-blue); font-weight: 700; font-size: 30px; letter-spacing: 0.5px;
  }
  .back-logo .mark { width: 18px; height: 18px; background: var(--brand-blue); }
  .divider {
    position: absolute; left: 292px; top: 58px; width: 2px; height: 196px;
    background: var(--brand-blue);
  }
  .details { position: absolute; left: 318px; top: 60px; }
  .person-name { color: var(--brand-blue); font-weight: 700; font-size: 22px; letter-spacing: 0.5px; }
  .person-role { font-size: 13px; margin-top: 2px; }
  .address { font-size: 14px; line-height: 1.45; margin-top: 14px; }
  .contacts { list-style: none; margin-top: 12px; font-size: 14px; }
  .contacts li { display: flex; align-items: center; gap: 8px; line-height: 1.6; }
  .contacts svg { width: 13px; height: 13px; fill: var(--brand-blue); flex: none; }
</style>
</head>
<body>
  <section class="card card-front">
    <div class="front-logo"><span class="mark"></span><span>HALDEN LAW</span></div>
    <p class="regulation-note">The firm is authorised and regulated by the KWT</p>
  </section>

  <section class="card card-back">
    <div class="back-logo"><span class="mark"></span><span>HALDEN LAW</span></div>
    <div class="divider"></div>
    <div class="details">
      <h1 class="person-name">THOMAS REED</h1>
      <p class="person-role">Managing Director</p>
      <p class="address">Your address, City<br>State, Zip 1234</p>
      <ul class="contacts">
        <li>
          <svg viewBox="0 0 16 16" aria-hidden="true"><path d="M3 1h3l1.5 4-2 1.2a9 9 0 0 0 4.3 4.3L11 8.5l4 1.5v3a2 2 0 0 1-2 2A12 12 0 0 1 1 3a2 2 0 0 1 2-2z"/></svg>
          <span>123 456 789</span>
        </li>
        <li>
          <svg viewBox="0 0 16 16" aria-hidden="true"><path d="M1 3h14v10H1z M1 3l7 6 7-6" stroke="#fff" stroke-width="1"/></svg>
          <span>info@haldenlaw.com</span>
        </li>
        <li>
          <svg viewBox="0 0 16 16" aria-hidden="true"><circle cx="8" cy="8" r="7"/><path d="M1 8h14M8 1c-3 3-3 11 0 14M8 1c3 3 3 11 0 14" stroke="#fff" stroke-width="1" fill="none"/></svg>
          <span>www.haldenlaw.com</span>
        </li>
      </ul>
    </div>
  </section>
</body>
</html>
```